Business Card Stationary for new Logo Skin Care Studio
BusinessCard, LetterHead, Envelope. EmailSignature, Tri-fold (background only)
Professional
Marisol Quenby
41726 Calle Ondulada #219
Mission Viejo, CA 92691
marisolquenby@postvelna.com
www.skinbymarisol.com
BusinessCard, LetterHead, Envelope. EmailSignature,
one page background (matching other stationary) that can be used for brochure
Thanks
no email address on business card!
two lines for :
next appointment;

```html
<!DOCTYPE html>
<html lang="en">
<head>
<meta charset="utf-8">
<title>Marisol's Skin Care Studio Stationery</title>
<link href="https://fonts.googleapis.com/css2?family=Poppins:wght@400;600;700&display=swap" rel="stylesheet">
<style>
  :root{
    --bg:#3b3b3b;
    --bg-dark:#2f2f2f;
    --paper:#ffffff;
    --green:#5fa821;
    --lime:#a8d13a;
    --orange:#f4a21c;
    --ink:#555555;
    --ink-soft:#8a8a8a;
  }
  *{box-sizing:border-box;margin:0;padding:0}
  html,body{width:1200px;height:310px;overflow:hidden}
  body{
    background:radial-gradient(ellipse at 50% 40%,var(--bg) 0%,var(--bg-dark) 100%);
    font-family:'Poppins',sans-serif;color:var(--ink);position:relative;
  }
  .piece{position:absolute;background:var(--paper);box-shadow:0 3px 8px rgba(0,0,0,.45);overflow:hidden}
  .wave{position:absolute;left:0;bottom:0;width:100%}
  .brand{display:flex;align-items:center;gap:4px}
  .brand-dot{border-radius:50%;background:var(--green);flex:none}
  .brand-name{font-weight:700;color:var(--green);line-height:1;white-space:nowrap}

  /* master logo */
  .master-logo{position:absolute;left:48px;top:18px;display:flex;flex-direction:column;align-items:center}
  .master-logo .brand-dot{width:30px;height:30px;margin-bottom:4px}
  .master-logo .brand-name{font-size:22px}
  .master-logo .tagline{font-size:8px;color:#cfcfcf;margin-top:4px;letter-spacing:.5px}

  /* business cards */
  .card{width:118px;height:50px}
  .card-front{left:19px;top:172px}
  .card-front .brand{position:absolute;left:6px;top:9px;flex-direction:column;gap:2px;width:50px}
  .card-front .brand-dot{width:8px;height:8px}
  .card-front .brand-name{font-size:8px}
  .card-front .details{position:absolute;left:62px;top:6px;width:52px;font-size:3.4px;line-height:4.8px;white-space:nowrap}
  .card-front .details strong{font-size:4.4px;color:var(--green)}
  .card-appt{left:19px;top:248px;padding:6px}
  .card-appt .heading{font-size:4.8px;font-weight:600;color:var(--green);margin-bottom:4px}
  .appt-line{font-size:3.8px;border-bottom:.6px solid #bbb;height:9px;width:100px;padding-top:3px}
  .card-services{left:144px;top:248px;padding:6px;background:linear-gradient(135deg,var(--lime),var(--green));color:#fff}
  .card-services .heading{font-size:5px;font-weight:600;margin-bottom:3px}
  .card-services p{font-size:3.8px}

  /* letterheads */
  .letterhead{width:178px;height:288px;top:17px;padding:12px}
  .lh-one{left:293px}
  .lh-two{left:490px}
  .letterhead .brand-dot{width:12px;height:12px}
  .letterhead .brand-name{font-size:12px}
  .lh-contact{position:absolute;right:12px;top:12px;font-size:3.8px;line-height:5.5px;width:66px;white-space:nowrap}
  .lh-mark{position:absolute;left:50%;top:50%;width:90px;height:90px;margin:-55px 0 0 -45px;border-radius:50%;background:radial-gradient(circle,rgba(168,209,58,.18),rgba(95,168,33,.05) 70%,transparent 72%)}
  .lh-foot{position:absolute;bottom:5px;left:0;width:100%;text-align:center;font-size:3.6px;color:#fff;z-index:2}

  /* small envelopes */
  .env-small{width:140px;height:86px;left:696px;padding:7px}
  .env-a{top:58px}
  .env-b{top:180px;height:78px}
  .env-small .brand-dot{width:8px;height:8px}
  .env-small .brand-name{font-size:8px}
  .env-small .ret{font-size:3.2px;line-height:4.3px;margin-top:3px}

  /* large envelopes */
  .env-large{width:182px;height:86px;left:852px}
  .env-orange{top:54px;background:var(--orange)}
  .env-green{top:118px;background:linear-gradient(180deg,var(--lime),var(--green))}
  .env-white{top:188px}
  .flap{position:absolute;left:0;top:0;width:100%;height:100%}
  .env-large .seal{position:absolute;left:50%;transform:translateX(-50%);display:flex;flex-direction:column;align-items:center}
  .env-large .brand-dot{width:12px;height:12px;background:#fff}
</style>
</head>
<body>

<div class="master-logo">
  <span class="brand-dot"></span>
  <span class="brand-name">Marisol's</span>
  <span class="tagline">Skin Care Studio</span>
</div>

<div class="piece card card-front">
  <div class="brand"><span class="brand-dot"></span><span class="brand-name">Marisol's</span></div>
  <div class="details">
    <strong>Marisol Quenby</strong><br>Licensed Esthetician<br>
    41726 Calle Ondulada #219<br>Mission Viejo, CA 92691<br>(949) 555-0143<br>www.skinbymarisol.com
  </div>
  <svg class="wave" viewBox="0 0 118 10" height="10" preserveAspectRatio="none"><path d="M0 6 Q40 0 118 5 V10 H0Z" fill="var(--lime)"/><path d="M0 8 Q50 3 118 7 V10 H0Z" fill="var(--green)"/></svg>
</div>

<div class="piece card card-appt">
  <div class="heading">Next Appointment:</div>
  <div class="appt-line">Date</div>
  <div class="appt-line">Time</div>
</div>

<div class="piece card card-services">
  <div class="heading">Our Services</div>
  <p>Facials · Peels · Waxing</p>
</div>

<div class="piece letterhead lh-one">
  <div class="brand"><span class="brand-dot"></span><span class="brand-name">Marisol's</span></div>
  <div class="lh-contact">Marisol Quenby<br>41726 Calle Ondulada #219<br>Mission Viejo, CA 92691<br>marisolquenby@postvelna.com</div>
  <div class="lh-mark" role="img" aria-label="Faint brand watermark"></div>
  <svg class="wave" viewBox="0 0 178 30" height="30" preserveAspectRatio="none"><path d="M0 14 Q70 2 178 12 V30 H0Z" fill="var(--orange)"/><path d="M0 18 Q80 6 178 16 V30 H0Z" fill="var(--lime)"/><path d="M0 22 Q90 12 178 20 V30 H0Z" fill="var(--green)"/></svg>
  <div class="lh-foot">www.skinbymarisol.com</div>
</div>

<div class="piece letterhead lh-two">
  <div class="brand"><span class="brand-dot"></span><span class="brand-name">Marisol's</span></div>
  <div class="lh-mark" role="img" aria-label="Faint brand watermark"></div>
  <svg class="wave" viewBox="0 0 178 30" height="30" preserveAspectRatio="none"><path d="M0 14 Q70 2 178 12 V30 H0Z" fill="var(--orange)"/><path d="M0 18 Q80 6 178 16 V30 H0Z" fill="var(--lime)"/><path d="M0 22 Q90 12 178 20 V30 H0Z" fill="var(--green)"/></svg>
  <div class="lh-foot">www.skinbymarisol.com</div>
</div>

<div class="piece env-small env-a">
  <div class="brand"><span class="brand-dot"></span><span class="brand-name">Marisol's</span></div>
  <div class="ret">41726 Calle Ondulada #219<br>Mission Viejo, CA 92691</div>
  <svg class="wave" viewBox="0 0 140 14" height="14" preserveAspectRatio="none"><path d="M0 7 Q60 0 140 6 V14 H0Z" fill="var(--lime)"/><path d="M0 10 Q70 4 140 9 V14 H0Z" fill="var(--green)"/></svg>
</div>
<div class="piece env-small env-b">
  <div class="brand"><span class="brand-dot"></span><span class="brand-name">Marisol's</span></div>
  <div class="ret">41726 Calle Ondulada #219<br>Mission Viejo, CA 92691</div>
  <svg class="wave" viewBox="0 0 140 14" height="14" preserveAspectRatio="none"><path d="M0 7 Q60 0 140 6 V14 H0Z" fill="var(--orange)"/><path d="M0 10 Q70 4 140 9 V14 H0Z" fill="var(--green)"/></svg>
</div>

<div class="piece env-large env-orange">
  <svg class="flap" viewBox="0 0 182 86" preserveAspectRatio="none"><path d="M0 0 L91 52 L182 0 V86 H0Z" fill="#fff"/></svg>
</div>
<div class="piece env-large env-green">
  <svg class="flap" viewBox="0 0 182 86" preserveAspectRatio="none"><path d="M0 0 L91 52 L182 0 V86 H0Z" fill="#fff"/></svg>
  <div class="seal" style="top:12px"><span class="brand-dot"></span></div>
</div>
<div class="piece env-large env-white">
  <svg class="flap" viewBox="0 0 182 86" preserveAspectRatio="none"><path d="M0 0 L91 50 L182 0" fill="none" stroke="#d6d6d6" stroke-width="1"/></svg>
</div>

</body>
</html>
```